We are looking for a 2-page (front and back) 3.67" x 8.5" rack card. . Please refer back to our other Rack Cards for a similar look and feel to the card. This one is titled: Myths and Truths About Memory Loss
The document is for older readers. Do not put text over graphics and keep it simple and easy to read with high contrast.
We want some very simple design element(s) incorporated that convey Native American communities or heritage. But NO headdress, teepee graphics, owls etc. I have included some graphics, please use your creative discretion to use which ones look good on the cards. Please remember to include the funding statement - it can be in a very small font 6/7 point. For more information about our project, please visit https://orvelmesa.net/mind-care/library - This rack card is supported by the Bureau for Wellness Tracking and Outreach (BWT) of the Federal Office of Family and Care Affairs (FOF) as part of a financial assistance award totaling $1,053,119.36 with 100 percent funded by BWT/FOF. The contents are those of the author(s) and do not necessarily represent the official views of, nor an endorsement, by BWT/FOF, or the U.S. Government.
Please feel free to choose one of each of the 2 logos that looks best. We have the QT7 logo and the Mind Wellness Support Hub logo we would like to add. I have added the document and there are images to choose from to use in the rack card. We definitely want to incorporate the coyote in this rack card since it is culturally significant.

```html
<!DOCTYPE html>
<html lang="en">
<head>
<meta charset="utf-8">
<title>Myths and Truths About Memory Loss – Rack Card</title>
<link rel="stylesheet" href="https://fonts.googleapis.com/css2?family=Archivo:wght@700;800;900&family=Jost:ital,wght@0,400;0,500;0,700;1,400;1,500&display=swap">
<style>
  :root{
    --page:#e6e6e6;
    --white:#ffffff;
    --maroon:#6b1f1a;
    --maroon-dark:#5c1d18;
    --teal:#1f7575;
    --teal-deep:#1d6f70;
    --teal-light:#52a6ae;
    --clay:#b7685b;
    --ink-red:#6e2a24;
    --ink-teal:#236f73;
  }
  *{box-sizing:border-box;margin:0;padding:0}
  html,body{width:1200px;height:1200px;overflow:hidden;background:var(--page)}
  body{position:relative;font-family:"Jost",sans-serif}
  .card{position:absolute;top:121px;width:413px;height:957px;background:var(--white);overflow:hidden}
  .card--front{left:171px}
  .card--back{left:636px}
  .photo{position:absolute;left:0;width:100%}
  .photo--regalia{top:0;height:135px;background:linear-gradient(180deg,#e9a6c9 0%,#e0479a 30%,#9d56b4 55%,#5a74c9 75%,#a9c6e6 100%)}
  .photo--canyon{top:0;height:135px;background:linear-gradient(180deg,#9fb6cc 0%,#f1d6a7 26%,#c67c58 46%,#a9584a 68%,#6a8e98 84%,#b0755a 100%)}
  .photo--elders{top:753px;height:163px;background:linear-gradient(120deg,#8b6a4d 0%,#b59a7d 35%,#4a5f8e 60%,#9aa3ae 85%,#c9b49a 100%)}
  .title{position:absolute;left:31px;top:146px;width:351px;font-family:"Archivo",sans-serif;font-weight:900;font-size:31.5px;line-height:33px;letter-spacing:-.2px}
  .title span{display:block}
  .title .t1{color:var(--maroon)}
  .title .t2{color:var(--teal)}
  .title-rule{position:absolute;left:31px;top:334px;width:351px;height:3px;background:var(--teal)}
  .intro{position:absolute;left:31px;top:343px;width:355px;font-size:15.2px;line-height:18.7px;color:#222}
  .mvt{position:absolute;left:0;width:100%;height:36px;display:flex}
  .mvt .myth{flex:0 0 207px;background:var(--clay);color:var(--white);text-align:right;padding-right:30px}
  .mvt .truth{flex:1;background:var(--teal-light);color:var(--white);padding-left:30px}
  .mvt .myth,.mvt .truth{font-family:"Archivo",sans-serif;font-weight:900;font-size:25px;line-height:36px;letter-spacing:.5px}
  .mvt .vs{position:absolute;left:186px;top:-4px;width:44px;height:44px;border-radius:50%;background:var(--white);color:var(--teal-light);font-family:"Archivo",sans-serif;font-weight:900;font-size:20px;line-height:44px;text-align:center}
  .card--front .mvt{top:478px}
  .card--back .mvt{top:135px;}
  .pairs{position:absolute;left:31px;width:351px}
  .pair{display:flex;border-top:1.5px solid var(--teal-light)}
  .pair:first-child{border-top:none}
  .pair p{font-size:12.6px;line-height:15.6px;padding-top:8px}
  .pair .m{flex:0 0 176px;color:var(--ink-red);padding-right:10px;border-right:1.5px solid var(--teal-light)}
  .pair .t{flex:1;color:var(--ink-teal);padding-left:15px}
  .card--front .pairs{top:514px}
  .card--back .pairs{top:172px}
  .weave{position:absolute;left:0;width:100%;height:20px;background:linear-gradient(180deg,#ffffff 0%,#d8b5ae 35%,#a9d0d4 65%,#ffffff 100%)}
  .card--front .weave{top:637px}
  .card--back .weave{top:469px}
  .quote{position:absolute;left:0;top:658px;width:100%;height:95px;background:var(--teal-deep);color:var(--white)}
  .quote .mark{position:absolute;font-family:"Jost",sans-serif;font-weight:700;font-style:italic;font-size:30px;line-height:1}
  .quote .mark--open{left:24px;top:10px}
  .quote .mark--close{left:370px;top:27px}
  .quote blockquote{position:absolute;left:54px;top:9px;width:305px;font-style:italic;font-size:13.4px;line-height:17px;text-align:center}
  .quote cite{position:absolute;left:46px;top:58px;font-style:italic;font-size:10.6px;line-height:17px;text-align:center;width:230px}
  .brand{position:absolute;right:20px;display:flex;align-items:center;gap:6px;font-family:"Jost",sans-serif;font-weight:700;color:var(--teal);font-size:13px;line-height:14px;text-align:left}
  .brand .dot{width:12px;height:12px;border-radius:50%;background:var(--teal)}
  .card--front .brand{top:858px;background:rgba(255,255,255,.92);padding:5px 7px}
  .card--back .brand{top:848px}
  .footer{position:absolute;left:0;bottom:0;width:100%;height:41px;background:var(--maroon-dark);color:var(--white);text-align:center;font-family:"Archivo",sans-serif;font-weight:800;font-size:16.5px;line-height:41px}
  .act{position:absolute;left:0;top:490px;width:100%;height:113px;background:var(--teal);color:var(--white);text-align:center;padding:14px 30px 0}
  .act h2{font-family:"Archivo",sans-serif;font-weight:900;font-size:17px;line-height:20px;margin-bottom:5px}
  .act p{font-size:12.8px;line-height:18px}
  .more{position:absolute;left:31px;top:613px;width:351px}
  .more h2{font-family:"Archivo",sans-serif;font-weight:900;font-size:16.2px;line-height:22px;color:var(--maroon);text-align:center;padding-bottom:2px;border-bottom:2.5px solid var(--maroon)}
  .link{text-align:center;margin-top:7px}
  .link h3{font-family:"Jost",sans-serif;font-weight:700;font-size:13px;line-height:17px;color:var(--ink-teal);margin-bottom:4px}
  .link .url{display:block;background:var(--teal-light);color:var(--white);border-radius:12px;font-size:11px;line-height:15.5px;padding:3px 18px}
  .funding{position:absolute;left:31px;top:824px;width:238px;font-size:7.7px;line-height:11.8px;color:#222}
</style>
</head>
<body>

<section class="card card--front">
  <div class="photo photo--regalia" role="img" aria-label="Photo of pink, purple and blue ribbon regalia beside a beaded medallion"></div>
  <h1 class="title"><span class="t1">MYTHS AND TRUTHS</span><span class="t2">ABOUT MEMORY LOSS</span></h1>
  <div class="title-rule"></div>
  <p class="intro">People sometimes believe things about memory loss that are not true. Misunderstandings can make it harder for Elders in Native communities to get the help they need when they start having memory issues. Below are some common myths and truths about memory loss, Alzheimer’s disease, and related dementias.</p>

  <div class="mvt"><div class="myth">MYTH</div><div class="vs">vs.</div><div class="truth">TRUTH</div></div>
  <div class="pairs">
    <div class="pair" style="height:38px"><p class="m">Getting Alzheimer’s is a normal part of aging.</p><p class="t">It is a disease that not everyone will get.</p></div>
    <div class="pair" style="height:113px"><p class="m">Memory problems and forgetfulness are definite signs of dementia.</p><p class="t">Memory problems do not solely determine if they are dementia. Other medical conditions can cause memory problems. Talk to your doctor.</p></div>
    <div class="pair" style="height:84px"><p class="m">Only older people can get Alzheimer’s disease.</p><p class="t">There have been cases for people as young as twenty-five, though it is rare to undergo treatment.</p></div>
  </div>
  <div class="weave" role="img" aria-label="Woven zigzag border in clay and teal"></div>

  <div class="quote">
    <span class="mark mark--open">“</span>
    <blockquote>The beauty in life is each day is a new day to try again and be a better version of myself than yesterday.</blockquote>
    <span class="mark mark--close">”</span>
    <cite>Marla Stonecrow (Blackfeet)<br>personal communication with the author.</cite>
  </div>
  <div class="photo photo--elders" role="img" aria-label="Photo collage of Elders in a circle outdoors, a smiling couple holding feathers, and a grandmother with children"></div>
  <div class="brand"><span class="dot"></span><span>QT7<br>ELDER CIRCLE</span></div>
  <div class="footer">www.orvelmesa.net</div>
</section>

<section class="card card--back">
  <div class="photo photo--canyon" role="img" aria-label="Photo of a red rock canyon river bend at sunrise"></div>
  <div class="mvt"><div class="myth">MYTH</div><div class="vs">vs.</div><div class="truth">TRUTH</div></div>
  <div class="pairs">
    <div class="pair" style="height:83px"><p class="m">People with Alzheimer’s disease cannot be happy.</p><p class="t">A person with memory loss can experience strong moods and emotions but still enjoy life and relationships.</p></div>
    <div class="pair" style="height:112px"><p class="m">Dementia can be prevented by a certain supplement or food.</p><p class="t">Healthy eating may help overall wellness, including brain health. No additional supplements will completely prevent the onset of dementia.</p></div>
    <div class="pair" style="height:102px"><p class="m">Alzheimer’s is reversible through prescription drugs.</p><p class="t">There are prescription drugs to address symptoms of Alzheimer’s and dementia, but there are no medicines that can reverse them.</p></div>
  </div>
  <div class="weave" role="img" aria-label="Woven zigzag border in clay and teal"></div>

  <div class="act">
    <h2>WHAT YOU CAN DO</h2>
    <p>If you or someone you love is having memory problems, do not wait. Talk to a healthy provider you trust. Learning the truth can help keep our Elders strong and supported.</p>
  </div>

  <div class="more">
    <h2>FOR MORE MYTH-BUSTING INFORMATION</h2>
    <div class="link"><h3>12 Common Alzheimer's Disease Myths on CareField.com</h3><span class="url">https://www.carefield.com/c/memory-myths-explained/</span></div>
    <div class="link"><h3>Memory Research Alliance Myths vs. Facts</h3><span class="url">https://www.memoryalliance.org/dementia/research-and-progress/clinical-studies/myths-vs-facts</span></div>
    <div class="link"><h3>QT7 Brain Health Resources</h3><span class="url">https://orvelmesa.net/resources/</span></div>
  </div>

  <p class="funding">This rack card is supported by the Bureau for Wellness Tracking and Outreach (BWT) of the Federal Office of Family and Care Affairs (FOF) as part of a financial assistance award totaling $1,053,119.36 with 100 percent funded by BWT/FOF. The contents are those of the author(s) and do not necessarily represent the official views of, nor an endorsement, by BWT/FOF, or the U.S. Government.</p>
  <div class="brand"><span class="dot"></span><span>QT7<br>ELDER CIRCLE</span></div>
  <div class="footer">www.orvelmesa.net</div>
</section>

</body>
</html>
```